Ledgerwise Systems Group business card design.

We are a software development company that develop Software for finance companies and related industries.

We need a 2 sided business card designed. We have a new logo already designed (see attached eps and ai) We are after a clean simple corporate look. One side with just our logo, and the second side with our details.

Mark Hollister
Managing Director

Suite 4 Level 9, 138 Kellaway Street Sydney NSW 2000

Direct: +61 2 9374 6021
Mobile: +61 4 2287 5196
Email: markh@lsg-example.net.au
Web: www.lsg-example.net.au

I have included 2 logo files an .ai and .eps. I noticed that the lines either side of the group looks a bit jaggered and needs to be made sharper.

I would like to introduce a little colour somewhere rather than having it all black and white. But not over the top, keeping with a simple clean corporate look. Perhaps a light blue on some of the text?

If you have other ideas would be pleased to review

Regards

Mark H.

```html
<!DOCTYPE html>
<html lang="en">
<head>
<meta charset="utf-8">
<title>Ledgerwise Systems Group – Business Card</title>
<link href="https://fonts.googleapis.com/css2?family=IBM+Plex+Sans:wght@400;600&display=swap" rel="stylesheet">
<style>
  :root {
    --backdrop: #e6e8ec;
    --card-white: #ffffff;
    --navy: #13264a;
    --navy-light: #2a4677;
    --text-navy: #1d3157;
    --text-muted: #4d5d7a;
    --rule: #8a97ad;
  }
  * { box-sizing: border-box; margin: 0; padding: 0; }
  html, body {
    width: 1200px; height: 1023px; overflow: hidden;
    background: var(--backdrop);
    font-family: "IBM Plex Sans", Arial, sans-serif;
  }
  .canvas {
    width: 1200px; height: 1023px;
    display: flex; align-items: center; justify-content: center; gap: 60px;
  }
  .card {
    width: 520px; height: 318px; position: relative; overflow: hidden;
    box-shadow: 0 10px 28px rgba(20, 30, 50, 0.25);
  }
  /* Details side */
  .card--details { background: var(--card-white); color: var(--text-navy); }
  .details__person { position: absolute; left: 38px; top: 34px; }
  .details__name { font-size: 25px; font-weight: 600; letter-spacing: 0.5px; }
  .details__title { font-size: 15px; color: var(--text-muted); margin-top: 2px; }
  .details__contacts { list-style: none; margin-top: 16px; }
  .details__contacts li {
    display: flex; align-items: center; gap: 10px;
    font-size: 15px; color: var(--text-muted); line-height: 24px;
  }
  .icon {
    width: 14px; height: 14px; border-radius: 2px; background: var(--navy);
    display: inline-flex; align-items: center; justify-content: center; flex: none;
  }
  .details__rule {
    position: absolute; left: 318px; top: 30px; width: 1px; height: 160px;
    background: var(--rule);
  }
  .details__address {
    position: absolute; left: 336px; top: 132px;
    font-size: 14px; line-height: 21px; color: var(--text-muted);
  }
  .details__band {
    position: absolute; left: 0; right: 0; bottom: 0; height: 92px;
    background: var(--navy);
  }
  .details__band-accent {
    position: absolute; left: 0; right: 0; bottom: 92px; height: 6px;
    background: var(--navy-light);
  }
  /* Brand side */
  .card--brand {
    background: linear-gradient(160deg, #1b3360 0%, var(--navy) 55%, #0e1d3a 100%);
    display: flex; align-items: center; justify-content: center; gap: 14px;
  }
  .brand__square { width: 22px; height: 22px; background: var(--navy-light); }
  .brand__name {
    font-size: 22px; font-weight: 600; letter-spacing: 1px; color: #c9d3e4;
  }
</style>
</head>
<body>
<main class="canvas">
  <section class="card card--details" aria-label="Business card, details side">
    <div class="details__person">
      <h1 class="details__name">Mark Hollister</h1>
      <p class="details__title">Managing Director</p>
      <ul class="details__contacts">
        <li><span class="icon"><svg width="10" height="10" viewBox="0 0 10 10"><path d="M2 1l2 2-1 1.2c.6 1.2 1.6 2.2 2.8 2.8L7 6l2 2-1.4 1.4C4.5 9 1 5.5.6 2.4z" fill="#fff"/></svg></span>+61 2 9374 6021</li>
        <li><span class="icon"><svg width="10" height="10" viewBox="0 0 10 10"><rect x="2.5" y="0.5" width="5" height="9" rx="1" fill="none" stroke="#fff"/><circle cx="5" cy="8" r=".6" fill="#fff"/></svg></span>+61 4 2287 5196</li>
        <li><span class="icon"><svg width="10" height="10" viewBox="0 0 10 10"><rect x=".5" y="2" width="9" height="6" fill="none" stroke="#fff"/><path d="M.5 2L5 5.5 9.5 2" fill="none" stroke="#fff"/></svg></span>markh@lsg-example.net.au</li>
        <li><span class="icon"><svg width="10" height="10" viewBox="0 0 10 10"><circle cx="5" cy="5" r="4.2" fill="none" stroke="#fff"/><path d="M.8 5h8.4M5 .8c-2 2.5-2 5.9 0 8.4M5 .8c2 2.5 2 5.9 0 8.4" fill="none" stroke="#fff" stroke-width=".8"/></svg></span>www.lsg-example.net.au</li>
      </ul>
    </div>
    <div class="details__rule"></div>
    <address class="details__address" style="font-style:normal">
      Suite 4 Level 9,<br>138 Kellaway Street<br>Sydney NSW 2000
    </address>
    <div class="details__band-accent"></div>
    <div class="details__band"></div>
  </section>

  <section class="card card--brand" aria-label="Business card, brand side">
    <span class="brand__square"></span>
    <span class="brand__name">Ledgerwise Systems Group</span>
  </section>
</main>
</body>
</html>
```